Brightwave Business Card

Professional Business Card Design required using the attached contact information.

Contact information can be rearranged as required.

The company is a new start up venture developing solar systems, the branding should be in keeping with that of one of the investors whose website is as follows https://www.quorvex.com/

```html
<!DOCTYPE html>
<html lang="en">
<head>
<meta charset="utf-8">
<title>Brightwave Renewables – Business Card</title>
<link href="https://fonts.googleapis.com/css2?family=Poppins:wght@400;500&family=Oswald:wght@500&display=swap" rel="stylesheet">
<style>
  :root {
    --backdrop: #1a1a1a;
    --card: #1f1f1f;
    --card-edge: #2a2a2a;
    --ink: #ffffff;
    --ink-soft: #e6e6e6;
    --accent: #2f7a66;
    --rule: #d9d9d9;
    --glow: rgba(255,255,255,0.035);
  }
  * { box-sizing: border-box; margin: 0; padding: 0; }
  html, body {
    width: 1200px; height: 1200px; overflow: hidden;
    background: var(--backdrop);
  }
  .stage {
    width: 1200px; height: 1200px;
    display: flex; flex-direction: column; align-items: center; justify-content: center;
    gap: 44px;
  }
  .card {
    position: relative;
    width: 840px; height: 480px;
    background: var(--card);
    border: 1px solid var(--card-edge);
    overflow: hidden;
    font-family: "Poppins", sans-serif;
    color: var(--ink);
  }
  .card__flare {
    position: absolute;
    width: 420px; height: 420px; border-radius: 50%;
    background: radial-gradient(circle, var(--glow) 0%, transparent 70%);
  }
  .card--front .card__flare { right: 20px; top: 30px; }
  .card--back .card__flare { right: -20px; top: 120px; }

  .wordmark {
    position: absolute;
    display: flex; align-items: center; gap: 14px;
    font-family: "Poppins", sans-serif;
    font-weight: 500;
    font-size: 27px;
    letter-spacing: 0.16em;
    text-transform: uppercase;
    color: var(--ink);
    white-space: nowrap;
  }
  .wordmark__dot {
    width: 12px; height: 12px; border-radius: 50%;
    background: var(--accent);
  }
  .card--front .wordmark { left: 210px; top: 210px; }
  .card--back .wordmark { left: 70px; top: 84px; }

  .card__rule {
    position: absolute;
    left: 70px; top: 290px;
    width: 460px; height: 1px;
    background: var(--rule);
  }
  .contact {
    position: absolute;
    left: 70px; top: 316px;
    list-style: none;
    font-size: 19px; line-height: 32px;
    color: var(--ink-soft);
  }
  .contact__item { display: flex; align-items: center; gap: 12px; }
  .contact__icon { width: 16px; height: 16px; fill: var(--accent); flex: none; }
  .holder {
    position: absolute;
    right: 70px; top: 296px;
    font-family: "Oswald", sans-serif;
    font-weight: 500;
    font-size: 30px;
    line-height: 1.2;
    letter-spacing: 0.06em;
    text-transform: uppercase;
    white-space: nowrap;
    color: var(--ink);
  }
</style>
</head>
<body>
<main class="stage">

  <section class="card card--front" aria-label="Card front">
    <div class="card__flare"></div>
    <div class="wordmark">Brightwave <span class="wordmark__dot"></span> Renewables</div>
  </section>

  <section class="card card--back" aria-label="Card back">
    <div class="card__flare"></div>
    <div class="wordmark">Brightwave <span class="wordmark__dot"></span> Renewables</div>
    <div class="card__rule"></div>
    <ul class="contact">
      <li class="contact__item">
        <svg class="contact__icon" viewBox="0 0 16 16"><path d="M3.6 1.5l2.2 2.6-1.3 1.6c.9 2 2.3 3.4 4.3 4.3l1.6-1.3 2.6 2.2-1.2 2.4C6.6 13.6 2.4 9.4 1.2 2.7z"/></svg>
        +1 (555) 014-2273
      </li>
      <li class="contact__item">
        <svg class="contact__icon" viewBox="0 0 16 16"><path d="M1 3h14v10H1z M2.2 4.2v.3L8 8.6l5.8-4.1v-.3z" fill-rule="evenodd"/></svg>
        daniel.marsh@brightwave-renewables.com
      </li>
      <li class="contact__item">
        <svg class="contact__icon" viewBox="0 0 16 16"><path d="M8 1a7 7 0 100 14A7 7 0 008 1zm0 1.4c.8 0 1.7 1.6 2 4H6c.3-2.4 1.2-4 2-4zM2.5 7.3h2.3c0 .5 0 1 .1 1.4H2.5a5.6 5.6 0 010-1.4zm3.5 0h4c0 .5 0 1-.1 1.4H6.1L6 7.3zm5.2 0h2.3a5.6 5.6 0 010 1.4h-2.4l.1-1.4zM6 9.6h4c-.3 2.4-1.2 4-2 4s-1.7-1.6-2-4z"/></svg>
        www.quorvex.com
      </li>
      <li class="contact__item">
        <svg class="contact__icon" viewBox="0 0 16 16"><path d="M8 1a5 5 0 00-5 5c0 3.6 5 9 5 9s5-5.4 5-9a5 5 0 00-5-5zm0 7a2 2 0 110-4 2 2 0 010 4z"/></svg>
        218 Harbor Street, Portland, ME 04101
      </li>
    </ul>
    <div class="holder">Daniel Marsh</div>
  </section>

</main>
</body>
</html>
```